Industry leading Property Management Company needs a flyer!

We need a brochure describing our fees and a basic description of what we do. This brochure will be printed, to be given to prospective clients, but we would also like an electronic version that can be downloaded from our website as a PDF. This project will be printed double sided, on standard 8.5" x 11" paper, in landscape mode, as a tri-fold brochure.

Target Market(s)

Real estate investors, but more importantly, first time investors. Many of our clients are "accidental landlords" who had their property for sale that didn't sell, so they are trying property management and rental investing for the first time. TRUST is their biggest fear

Font styles to use
Sans Serif

Requirements
Must have
• Must incorporate our logo, elements of our pricing list, and incorporate the text from our home page and "property management info" page (www.corvalinkrent.net). A word document specifying this text has been included in the project brief.
• Additionally, I am thinking this will be a simple, single piece of paper, in landscape mode, printed on both sides, in a Tri-fold. The front of the brochure will have the logo/name of the company, along with the Harbor Tenant Medals logos. I am thinking the first inside pane, when someone opens up the brochure, will have reference text #1 and #3. The 3 tiered pricing plan might occupy the 2nd and 3rd of the three panes on the inside fold. Reference text #4, 5, and 6 will occupy the next pane (see brief for handwritten layout). Then, the very back pane (when it is folded and shut) will have reference text #2 and our company contact information, plus any kind of stock photos, etc.
Nice to have
• Our main market will be first time investors, so we need to display and demonstrate relationships, and trust. We would prefer stock photos that incorporate families, children, or other images that solidify peace of mind.

```html
<!DOCTYPE html>
<html lang="en">
<head>
<meta charset="utf-8">
<title>Corvalink Property Management – Tri-fold Brochure</title>
<link rel="stylesheet" href="https://fonts.googleapis.com/css2?family=Montserrat:wght@400;500;600;700;800&family=Oswald:wght@400;500;600&display=swap">
<style>
:root{
  --bg:#e4e5e7;
  --blue:#1e88d6;
  --blue-deep:#0b5ea8;
  --blue-line:#8cc6f0;
  --dark:#2c2e31;
  --dark-2:#3a3c40;
  --white:#ffffff;
  --ink:#1f2a36;
  --muted:#c9d3dc;
  --red:#b3262d;
  --gold:#c99a2e;
}
*{box-sizing:border-box;margin:0;padding:0}
html,body{width:1053px;height:1200px;overflow:hidden;background:var(--bg);font-family:"Montserrat",Arial,sans-serif;color:var(--white)}
.canvas{position:relative;width:1053px;height:1200px}
.sheet{position:absolute;left:154px;width:745px;height:576px;display:flex;box-shadow:0 6px 18px rgba(0,0,0,.22)}
.sheet--outside{top:16px}
.sheet--inside{top:608px}
.panel{position:relative;height:100%;overflow:hidden}
.panel--third{width:248px}

/* outside: left info panel */
.panel--info{background:linear-gradient(180deg,var(--blue) 0%,var(--blue-deep) 100%);padding:22px 18px 0 18px}
.section-bar{display:flex;align-items:center;gap:6px;background:var(--white);color:var(--blue-deep);font-weight:800;font-size:11px;text-transform:uppercase;padding:6px 10px;margin:0 -18px 8px -18px;letter-spacing:.2px}
.section-bar .mark{width:10px;height:10px;background:var(--blue-deep)}
.panel--info p{font-size:7.4px;line-height:1.45;margin-bottom:7px}
.panel--info ul{list-style:none;font-size:7.4px;line-height:1.5;margin:0 0 7px 4px}
.panel--info ul li::before{content:"• "}
.lead-strong{font-weight:700;font-style:italic}

/* outside: middle dark panel */
.panel--why{background:var(--dark);padding:22px 20px 0 20px;text-align:center}
.why-title{color:var(--blue);font-weight:800;font-size:11px;line-height:1.25;text-transform:uppercase;margin-bottom:10px}
.panel--why p{font-size:7.4px;line-height:1.5;color:var(--muted);text-align:justify;margin-bottom:8px}
.why-square{width:58px;height:58px;background:var(--blue);margin:26px auto 16px}
.contact-title{color:var(--blue);font-weight:800;font-size:13px;letter-spacing:.5px;margin-bottom:10px}
.contact-lines{font-size:7.4px;line-height:1.6;color:var(--muted)}
.contact-lines b{color:var(--white)}
.skyline{position:absolute;left:0;right:0;bottom:0;height:140px;background:linear-gradient(180deg,rgba(44,46,49,0) 0%,#232427 60%,#1d1e20 100%)}

/* outside: cover */
.panel--cover{background:var(--white);color:var(--ink)}
.brand{display:flex;align-items:center;gap:8px;padding:22px 20px 0}
.brand-square{width:20px;height:20px;background:var(--blue-deep)}
.brand-name{font-weight:800;font-size:15px;color:var(--blue-deep);letter-spacing:.4px;line-height:1.1}
.brand-name small{display:block;font-size:7px;letter-spacing:1.6px}
.cover-photo{position:absolute;left:0;right:0;top:70px;height:380px;background:linear-gradient(160deg,#e9e6e1 0%,#cdbfae 45%,#8b7a68 100%);clip-path:polygon(0 6%,100% 0,100% 94%,0 100%)}
.award-badge{position:absolute;top:100px;left:70px;width:46px;height:46px;border-radius:50%;background:var(--gold);box-shadow:0 0 0 4px var(--red)}
.cover-url{position:absolute;bottom:30px;right:20px;font-weight:700;font-size:12px;color:var(--blue-deep)}

/* inside: services panel */
.panel--services{background:linear-gradient(180deg,var(--blue) 0%,var(--blue-deep) 100%);padding:26px 18px 0 24px}
.intro{font-weight:700;font-size:8.6px;line-height:1.4;margin-bottom:8px}
.service{display:flex;gap:12px;align-items:center;margin-top:12px}
.hex{flex:0 0 42px;width:42px;height:46px}
.service h3{font-weight:800;font-size:9px;text-transform:uppercase;text-decoration:underline;margin-bottom:3px}
.service p{font-size:7.4px;line-height:1.4}

/* inside: pricing */
.panel--pricing{width:497px;background:var(--dark);padding:20px 22px 0 22px;color:var(--white)}
.pricing-tab{display:flex;align-items:center;gap:10px;background:var(--blue);margin:0 140px 10px 0;padding:5px 14px;clip-path:polygon(0 0,100% 0,94% 100%,6% 100%)}
.pricing-tab strong{font-family:"Oswald",sans-serif;font-weight:600;font-size:17px;letter-spacing:.5px}
.pricing-tab span{font-size:7.4px;line-height:1.3}
.plans{width:100%;border-collapse:collapse;background:var(--blue);font-family:"Oswald",sans-serif;font-size:7px}
.plans th,.plans td{border:1px solid var(--blue-line);padding:2px 5px;height:16px}
.plans thead th{font-weight:500;vertical-align:top;height:64px;line-height:1.3;text-align:center;font-size:7px}
.plans thead th.label-head{background:transparent}
.plans thead th b{display:block;font-weight:600;font-size:8px}
.plans thead th em{font-style:normal;font-size:5.6px;opacity:.85;display:block;margin-bottom:3px}
.plans td.feature{width:200px;text-align:left}
.plans td.dot{text-align:center;width:92px}
.plans td.dot::after{content:"";display:inline-block;width:4px;height:4px;border-radius:50%;background:var(--white)}
.plans td.dot.none::after{display:none}
.popular{position:absolute;top:20px;left:310px;width:90px;background:var(--blue-deep);font-family:"Oswald",sans-serif;font-size:8px;text-align:center;padding:3px 0;letter-spacing:.5px}
.footnotes{margin-top:9px;font-size:6.2px;line-height:1.5;color:var(--muted)}
.footnotes p{margin-bottom:3px}
</style>
</head>
<body>
<main class="canvas">

  <!-- OUTSIDE OF BROCHURE -->
  <section class="sheet sheet--outside">
    <div class="panel panel--third panel--info">
      <h2 class="section-bar"><span class="mark"></span>Our Portfolio</h2>
      <p>Corvalink has distinguished itself as a leader in the management of smaller buildings: single family homes, duplexes, multi-unit buildings, smaller apartment blocks and single owner condominium units.</p>
      <p>Unlike large apartment blocks that give a rental discount to a caretaker to perform traditional property management duties, smaller buildings are more labour intensive and require a more "hands on" approach.</p>
      <p>Using the latest technology and specially trained field staff, Corvalink is able to efficiently manage your investment.</p>
      <h2 class="section-bar"><span class="mark"></span>Tenant Happiness &amp; Retention</h2>
      <p>At Corvalink, we believe we have two sets of clients: The Property Owner and the Tenant. A successful investment begins with finding a great tenant, but it doesn't end there!</p>
      <p class="lead-strong">We make a significant effort to keep tenants happy through:</p>
      <ul>
        <li>Great Customer Service</li>
        <li>Good communications</li>
        <li>Tenant loyalty and retention programs</li>
      </ul>
      <p>Creating happy tenants increase the likelihood they will sign their lease renewal, increasing the owners cashflow, reducing vacancies and minimizing turnover costs: A "Win-Win" for everyone involved.</p>
      <h2 class="section-bar"><span class="mark"></span>Transparency &amp; Reporting</h2>
      <p>One of the biggest sources of stress to an owner using a property management company is the "unknown".</p>
      <p>At Corvalink we go to great lengths to ensure there are no surprises. We ask your permission prior to sending out a contractor to repair an issue (except emergencies, of course) and our state-of-the-art maintenance system will keep you, and your tenant updated every step of the way.</p>
      <p>We give you access to an online portal so you can view your property's information anytime, but also send you a complete set of financial reports on a monthly basis.</p>
    </div>

    <div class="panel panel--third panel--why">
      <h2 class="why-title">Why choose Corvalink as your property management company</h2>
      <p>Corvalink has been recognized and voted multiple times as Winnipeg's Best Property Management Company by Harbor Tenant Medals. We are intently focussed on serving both owners and tenants and are dedicated to a culture of superior customer service.</p>
      <p>Whether you own one investment property or ten, the partnership process with Corvalink Property Management is easy, efficient and rewarding.</p>
      <div class="why-square"></div>
      <h2 class="contact-title">CONTACT US</h2>
      <div class="contact-lines">
        C-214 Alder Ridge Rd, Winnipeg, MB R2K 0P7<br>
        <b>TEL :</b> 204-555-0148 <b>FAX:</b> 1-888-555-0172<br>
        hello@corvalinkrent.net<br>
        www.corvalinkrent.net
      </div>
      <div class="skyline" role="img" aria-label="Faint city skyline silhouette"></div>
    </div>

    <div class="panel panel--third panel--cover">
      <div class="brand">
        <span class="brand-square"></span>
        <div class="brand-name">CORVALINK<small>PROPERTY MANAGEMENT</small></div>
      </div>
      <div class="cover-photo" role="img" aria-label="Photo of a property manager welcoming a family with children into a bright home"></div>
      <div class="award-badge" role="img" aria-label="Harbor Tenant Medals award badge"></div>
      <div class="cover-url">corvalinkrent.net</div>
    </div>
  </section>

  <!-- INSIDE OF BROCHURE -->
  <section class="sheet sheet--inside">
    <div class="panel panel--third panel--services">
      <p class="intro">Corvalink Property Management has been serving the Winnipeg and surrounding areas since 1997. We offer world class management services to investors and tenants in the single family and multifamily rental market.</p>
      <p class="intro">Corvalink Property Management in Winnipeg offers some of the most premium services available for investors and tenants.</p>

      <div class="service">
        <svg class="hex" viewBox="0 0 42 46"><polygon points="21,1 40,12 40,34 21,45 2,34 2,12" fill="#3d4044" stroke="#6b7076" stroke-width="2"/><path d="M12 24 L21 16 L30 24 M14 22 V31 H28 V22" fill="none" stroke="#fff" stroke-width="1.6"/></svg>
        <div><h3>Property Management</h3><p>Using the latest technology and specially trained staff, we efficiently manage your property.</p></div>
      </div>
      <div class="service">
        <svg class="hex" viewBox="0 0 42 46"><polygon points="21,1 40,12 40,34 21,45 2,34 2,12" fill="#3d4044" stroke="#6b7076" stroke-width="2"/><path d="M13 21 A9 9 0 0 1 29 19 M29 25 A9 9 0 0 1 13 27" fill="none" stroke="#fff" stroke-width="1.6"/><path d="M29 14 V19 H24 M13 32 V27 H18" fill="none" stroke="#fff" stroke-width="1.6"/></svg>
        <div><h3>Leasing &amp; Renewals</h3><p>We perform a comprehensive rental market evaluation to maximize your investment.</p></div>
      </div>
      <div class="service">
        <svg class="hex" viewBox="0 0 42 46"><polygon points="21,1 40,12 40,34 21,45 2,34 2,12" fill="#3d4044" stroke="#6b7076" stroke-width="2"/><path d="M13 15 L29 31 M29 15 L13 31" stroke="#fff" stroke-width="2"/></svg>
        <div><h3>Property Maintenance</h3><p>You'll never have to worry about that midnight call or have to scramble to find a plumber.</p></div>
      </div>
      <div class="service">
        <svg class="hex" viewBox="0 0 42 46"><polygon points="21,1 40,12 40,34 21,45 2,34 2,12" fill="#3d4044" stroke="#6b7076" stroke-width="2"/><path d="M12 32 H30 M12 32 V16 M15 29 L28 16" fill="none" stroke="#fff" stroke-width="1.6"/></svg>
        <div><h3>Rehab &amp; Construction</h3><p>We provide maintenance and repair services, and can also help you with larger construction projects.</p></div>
      </div>
      <div class="service">
        <svg class="hex" viewBox="0 0 42 46"><polygon points="21,1 40,12 40,34 21,45 2,34 2,12" fill="#3d4044" stroke="#6b7076" stroke-width="2"/><circle cx="21" cy="23" r="9" fill="none" stroke="#fff" stroke-width="1.6"/><path d="M16 23 L20 27 L27 19" fill="none" stroke="#fff" stroke-width="1.8"/></svg>
        <div><h3>Free Stuff</h3><p>At Corvalink we want to help smaller landlords. We believe in "giving back" which is why we volunteer hundreds of hours per year.</p></div>
      </div>
    </div>

    <div class="panel panel--pricing">
      <div class="pricing-tab"><strong>PRICING</strong><span>Complete transparency.<br>No locked in contracts *</span></div>
      <div class="popular">MOST POPULAR</div>
      <table class="plans">
        <thead>
          <tr>
            <th class="label-head"></th>
            <th><b>"No More Midnight Phone Calls"</b><em>(Property Maintenance)</em>$54 monthly admin fee +<br>$25 Maintenance Coordination Fee<br>= $79 per month</th>
            <th><b>"Full Service Management"</b><em>(Maintenance plus Full Tenant Management)</em>$130 monthly management fee** +<br>$25 Maintenance Coordination Fee<br>= $155 per month</th>
            <th><b>"Peace of Mind"</b><em>(Full service plus court protection)</em>$130 monthly management fee** +<br>$25 Maintenance Coordination Fee +<br>$30 Court protection package***<br>= $185 per month</th>
          </tr>
        </thead>
        <tbody>
          <tr><td class="feature">24/7 emergency call centre and dispatch</td><td class="dot"></td><td class="dot"></td><td class="dot"></td></tr>
          <tr><td class="feature">Tenant can create online maintenance tickets</td><td class="dot"></td><td class="dot"></td><td class="dot"></td></tr>
          <tr><td class="feature">Automatic maintenance owner notifications</td><td class="dot"></td><td class="dot"></td><td class="dot"></td></tr>
          <tr><td class="feature">Owner asked for permission before proceeding (except emergencies)</td><td class="dot"></td><td class="dot"></td><td class="dot"></td></tr>
          <tr><td class="feature">Chat interface for all parties to communicate</td><td class="dot"></td><td class="dot"></td><td class="dot"></td></tr>
          <tr><td class="feature">Customer service survey sent to every tenant after completion of job</td><td class="dot"></td><td class="dot"></td><td class="dot"></td></tr>
          <tr><td class="feature">Actual contractor invoices uploaded into online owner portal</td><td class="dot"></td><td class="dot"></td><td class="dot"></td></tr>
          <tr><td class="feature">Access to investor For Sale property listings (no commissions)</td><td class="dot"></td><td class="dot"></td><td class="dot"></td></tr>
          <tr><td class="feature">Accounting and reporting</td><td class="dot"></td><td class="dot"></td><td class="dot"></td></tr>
          <tr><td class="feature">Owner anonymity</td><td class="dot none"></td><td class="dot"></td><td class="dot"></td></tr>
          <tr><td class="feature">Portfolio management</td><td class="dot none"></td><td class="dot"></td><td class="dot"></td></tr>
          <tr><td class="feature">Tenant management</td><td class="dot none"></td><td class="dot"></td><td class="dot"></td></tr>
          <tr><td class="feature">Rent collection</td><td class="dot none"></td><td class="dot"></td><td class="dot"></td></tr>
          <tr><td class="feature">Warning letters, follow-up inspections, contracted disputes</td><td class="dot none"></td><td class="dot"></td><td class="dot"></td></tr>
          <tr><td class="feature">Meter readings</td><td class="dot none"></td><td class="dot"></td><td class="dot"></td></tr>
          <tr><td class="feature">Lease management</td><td class="dot none"></td><td class="dot"></td><td class="dot"></td></tr>
          <tr><td class="feature">Accounting and reporting</td><td class="dot none"></td><td class="dot"></td><td class="dot"></td></tr>
          <tr><td class="feature">Eligible for Group Insurance Plan (~45% discount off retail)</td><td class="dot none"></td><td class="dot"></td><td class="dot"></td></tr>
          <tr><td class="feature">Court protection ***</td><td class="dot none"></td><td class="dot none"></td><td class="dot"></td></tr>
        </tbody>
      </table>
      <div class="footnotes">
        <p>* Our management contracts have no term. If you find we are not a good fit for you, stop anytime.</p>
        <p>** Our fees are charged out at a flat rate. $130 is the maximum price for a single family home. Discounts are given for multiple units in the same building (i.e. $114 per unit for a duplex) and investors with multiple houses qualify for further discounts (eg: investor with 5 houses pay $110 per house, per month). Management fees are NOT charged if the unit is vacant.</p>
        <p>*** Court protection includes all costs if it is necessary to take the tenant to court over unpaid rent or an eviction for noise complaints, etc. Typical court costs are approximately $650 or more.</p>
      </div>
    </div>
  </section>

</main>
</body>
</html>
```